依頼詳細
ホテル内レストランなので、高級感ラグジュアリー感のあるデザイン希望

ターゲット:ホテルご宿泊者様向け

・ディナーご利用時1ドリンクサービス
・カラオケ個室完備
・パーティー
記載項目
社名:株式会社ミルトフォレスト
店舗名:KAEDE NOGIZAKAA
住所: 〒107-0061 東京都港区北青山5-27-9アパホテル&リゾート〈六本木駅東〉1階
TEL/FAX 03-6781-2294
サイズ
A6
ページ数
片面
希望イメージ
シンプル 複雑
単色 カラフル
暗い 明るい
日常 高級
遊び心 厳粛
未来的 伝統的
女性的 男性的
希望する色
設定なし
納品ファイル
• 高解像度JPG (.jpg)
• イラストレーター形式 (.ai)
• PNG形式 (.png)
補足説明
本コンペ入選者でランチ半額のチラシを依頼したく思っております。よろしくお願いします。
記載いただきたい内容の文言追記します。
写真も店内写真とビュッフェ写真を追加します。よろしくお願いいたします。

・パーティー
→3,000円/ブッフェ+free drink

→5,000円/ブッフェ+freedrink

→1万円/ブッフェ+freedrink

※貸切
・30名以上/15万円以上/2時間
追加料金→30分..1万円/1時間..2万円

・カラオケ→1時間..大7,000円/小5,000円

※予算・内容に応じてご予約承ります。
■ 選んだ理由

コンセプトのマッチと表現方法、今後展開したいイメージにあっているため、選ばせていただきました。チラシをぱっとみて、何を伝えたいのかが読み取りやすい構成が素晴らしいと感じました。

■ 提案者全員のお礼・コメント

今回たくさんの方にご提案いただき本当にありがとうございました。弊社複数の事業展開をしており、
新店もぞくぞくオープンしていくので、広告需要が高いです。今後ともみなさまからのご提案を何卒よろしくお願いいたします!

```html
<!DOCTYPE html>
<html lang="ja">
<head>
<meta charset="utf-8">
<title>KAEDE NOGIZAKAA パーティープラン</title>
<link rel="stylesheet" href="https://fonts.googleapis.com/css2?family=Noto+Serif+JP:wght@400;600;700&family=Great+Vibes&display=swap">
<style>
  :root {
    --ink: #0c0b0a;
    --deep: #141210;
    --gold: #d8b56a;
    --gold-light: #f0d9a2;
    --gold-dark: #a9823c;
    --red: #a8161c;
    --red-dark: #7a0d12;
    --white: #f7f3ea;
    --muted: #cfc7b8;
  }
  * { margin: 0; padding: 0; box-sizing: border-box; }
  html, body { width: 865px; height: 1200px; overflow: hidden; background: var(--ink); }
  .flyer {
    position: relative;
    width: 865px; height: 1200px;
    overflow: hidden;
    font-family: "Noto Serif JP", serif;
    color: var(--white);
    background: var(--ink);
  }
  .hero-photo {
    position: absolute; left: 0; top: 0; width: 865px; height: 980px;
    background:
      radial-gradient(ellipse 40% 30% at 48% 42%, rgba(120,70,40,.55), transparent 70%),
      radial-gradient(ellipse 60% 25% at 50% 62%, rgba(90,70,55,.7), transparent 75%),
      linear-gradient(180deg, #2a2320 0%, #3a2e26 35%, #241d19 60%, #0f0d0c 85%, var(--ink) 100%);
  }
  .drink-banner {
    position: absolute; left: 70px; top: 0; width: 250px; height: 200px;
  }
  .drink-banner .text {
    position: absolute; inset: 0; padding-top: 30px;
    text-align: center; color: var(--gold-light);
    font-weight: 700; line-height: 1.25;
  }
  .drink-banner .small { font-size: 26px; }
  .drink-banner .large { font-size: 34px; }
  .tagline {
    position: absolute; right: 50px; top: 50px;
    height: 540px;
    writing-mode: vertical-rl;
    font-size: 34px; font-weight: 600; letter-spacing: 1px; line-height: 1;
    color: var(--gold);
    white-space: nowrap;
    text-shadow: 0 2px 6px rgba(0,0,0,.6);
  }
  .title {
    position: absolute; left: 0; width: 865px; top: 470px;
    text-align: center;
    font-family: "Great Vibes", cursive;
    font-size: 140px; font-weight: 400; color: var(--gold);
    text-shadow: 0 3px 10px rgba(0,0,0,.5);
  }
  .reserve-badge {
    position: absolute; left: 665px; top: 600px; width: 118px; height: 118px;
    border-radius: 50%;
    background: radial-gradient(circle at 35% 30%, var(--gold-light), var(--gold) 55%, var(--gold-dark));
    display: flex; align-items: center; justify-content: center; text-align: center;
    color: var(--red-dark); font-weight: 700; font-size: 24px; line-height: 1.3;
  }
  .intro {
    position: absolute; left: 0; width: 865px; top: 730px;
    text-align: center; font-size: 25px; line-height: 1.75; font-weight: 600;
  }
  .karaoke {
    position: absolute; left: 0; width: 865px; top: 845px;
    text-align: center; font-size: 25px; font-weight: 600;
  }
  .footer {
    position: absolute; left: 0; top: 985px; width: 865px; height: 215px;
    background: var(--deep);
    border-top: 1px solid rgba(216,181,106,.35);
  }
  .brand {
    position: absolute; left: 50px; top: 40px; width: 150px;
    text-align: center; color: var(--gold);
  }
  .brand .mark {
    width: 56px; height: 56px; border-radius: 50%;
    border: 2px solid var(--gold); margin: 0 auto 12px;
  }
  .brand .name { font-size: 28px; font-weight: 600; letter-spacing: 3px; }
  .contact {
    position: absolute; left: 235px; top: 34px;
    font-size: 19px; line-height: 1.55; color: var(--white); font-style: normal;
  }
  .contact .tel { font-size: 21px; margin-top: 4px; }
</style>
</head>
<body>
<main class="flyer">
  <div class="hero-photo" role="img" aria-label="ホテルバーのカウンターに赤ワインと白ワインのグラス、ワインボトルが並ぶ写真"></div>

  <div class="drink-banner">
    <svg width="250" height="200" viewBox="0 0 250 200" aria-hidden="true">
      <polygon points="0,0 250,0 250,190 125,160 0,190" fill="var(--red)"/>
      <polygon points="8,0 242,0 242,180 125,152 8,180" fill="none" stroke="var(--gold)" stroke-width="1.5"/>
    </svg>
    <div class="text">
      <div class="small">ディナーご利用時</div>
      <div class="large">1ドリンク<br>サービス</div>
    </div>
  </div>

  <h2 class="tagline">ワンランク上のパーティープラン</h2>

  <h1 class="title">Party plan</h1>

  <div class="reserve-badge">ご予約<br>承り中</div>

  <p class="intro">各種パーティー・結婚式の二次会・交流会・忘年会・新年会等、<br>様々なシーンにお使いいただける空間をご用意しております。</p>

  <p class="karaoke">カラオケ個室 2部屋完備</p>

  <footer class="footer">
    <div class="brand">
      <div class="mark"></div>
      <div class="name">KAEDE</div>
    </div>
    <address class="contact">
      株式会社ミルトフォレスト<br>
      KAEDE NOGIZAKAA<br>
      〒107-0061<br>
      東京都港区北青山5-27-9 ルミエスホテル&amp;スイート〈青山駅北〉1階<br>
      <span class="tel">TEL/FAX 03-6781-2294</span>
    </address>
  </footer>
</main>
</body>
</html>
```